Etiketten für Imkerei aus der Steiermark
Zielgruppe
Wir sind eine Imkerei aus der Steiermark / Österreich im Vollerwerb. www.lindtal-honig.at
Zielgruppe: Frauen, Familien, Regional
Unser Image: hohe Qualität, Familienbetrieb, naturnah, gesund
Vermarktung: Direkt, Verkaufsstellen, Märkte, zukünftig auch online
Aufgabenstellung
Wir werden die Honiggläser und die Druckerei umstellen und möchten hierfür ein profesionelles abgestimmtes Design. Unser Logo soll erhalten bleiben. Die Honigsortenbezeichnung (Waldhonig, Cremehonig, Blütenhonig) soll zukünftig eingedruckt werden und neben dem Logo ein Zentrales Element sein.
In Zukunft verwenden wir Vorsa Gläser mit hohen Deckel der Firma Balumo in den Größen 1000g(Ilka 785), 500g (Vor 410), 250 g (Vor 212) und 150 g (Vor 125). Der Deckel soll einheitlich Gold oder Silber sein.

```html
<!DOCTYPE html>
<html lang="de">
<head>
<meta charset="utf-8">
<title>Etiketten Lindtal Honig</title>
<link href="https://fonts.googleapis.com/css2?family=Amatic+SC:wght@700&family=Open+Sans:wght@400;700&family=PT+Sans+Narrow&display=swap" rel="stylesheet">
<style>
  :root {
    --bg: #dcdcdc;
    --paper: #ffffff;
    --ink: #2b2b2b;
    --ink-soft: #555555;
    --wald: #2a8040;
    --bluete: #d0525a;
    --creme: #e2c15a;
    --honey: #fbe96a;
    --honey-edge: #2b2b2b;
  }
  * { margin: 0; padding: 0; box-sizing: border-box; }
  html, body { width: 897px; height: 1200px; overflow: hidden; background: var(--bg); }
  .sheet { position: absolute; left: 32px; top: 257px; width: 833px; height: 690px; }

  .size-caption {
    position: absolute; transform: translateX(-50%);
    font-family: "Open Sans", sans-serif; font-size: 11px; letter-spacing: 1.6px;
    color: #4a4a4a; white-space: nowrap;
  }

  .label { position: absolute; background: var(--paper); color: var(--ink); }
  .label > * { position: absolute; }
  .variety {
    left: 0; right: 0; text-align: center; transform: translateY(-50%);
    font-family: "Amatic SC", cursive; font-weight: 700; line-height: 1; color: #333;
  }
  .quality-band {
    left: 50%; transform: translate(-50%, -50%);
    font-family: "Open Sans", sans-serif; color: #fff; text-align: center;
    letter-spacing: 0.5px; white-space: nowrap;
  }
  .wald .quality-band { background: var(--wald); }
  .bluete .quality-band { background: var(--bluete); }
  .creme .quality-band { background: var(--creme); }
  .weight {
    left: 0; right: 0; text-align: center; transform: translateY(-50%);
    font-family: "Open Sans", sans-serif; font-weight: 700;
  }
  .brand {
    left: 50%; transform: translate(-50%, -50%);
    display: flex; flex-direction: column; align-items: center;
  }
  .brand-dot { border-radius: 50%; background: var(--honey); border: 1px solid var(--honey-edge); }
  .brand-name {
    font-family: "Open Sans", sans-serif; font-weight: 700; color: var(--ink);
    white-space: nowrap; line-height: 1.1; text-align: center;
  }
  .web {
    left: 0; right: 0; text-align: center; transform: translateY(-50%);
    font-family: "Open Sans", sans-serif; font-weight: 700;
  }
  .contact, .storage {
    font-family: "PT Sans Narrow", sans-serif; color: var(--ink-soft);
  }
  .storage { text-align: right; }
  .storage .best-before { display: block; }

  /* 100 x 60 mm */
  .s60 { width: 343px; height: 205px; }
  .s60 .variety { top: 38px; font-size: 36px; }
  .s60 .quality-band { top: 67px; width: 191px; height: 16px; font-size: 10.5px; line-height: 16px; }
  .s60 .weight { top: 86px; font-size: 9px; }
  .s60 .brand { top: 146px; }
  .s60 .brand-dot { width: 34px; height: 34px; margin-bottom: 3px; }
  .s60 .brand-name { font-size: 10px; }
  .s60 .web { top: 189px; font-size: 7px; }
  .s60 .contact { left: 11px; top: 147px; font-size: 7.6px; line-height: 9.3px; }
  .s60 .storage { right: 12px; top: 147px; font-size: 7.6px; line-height: 9.3px; }
  .s60 .storage .best-before { margin-top: 6px; font-size: 7px; }

  /* 120 x 100 mm */
  .s100 { width: 411px; height: 342px; }
  .s100 .variety { top: 82px; font-size: 44px; }
  .s100 .quality-band { top: 113px; width: 200px; height: 17px; font-size: 11px; line-height: 17px; }
  .s100 .weight { top: 135px; font-size: 9.5px; }
  .s100 .brand { top: 250px; }
  .s100 .brand-dot { width: 62px; height: 62px; margin-bottom: 5px; }
  .s100 .brand-name { font-size: 16px; }
  .s100 .web { top: 318px; font-size: 7px; }
  .s100 .contact { left: 21px; top: 277px; font-size: 7.6px; line-height: 9.3px; }
  .s100 .storage { right: 21px; top: 277px; font-size: 7.6px; line-height: 9.3px; }
  .s100 .storage .best-before { margin-top: 6px; font-size: 7px; }

  /* 100 x 45 mm */
  .s45 { width: 342px; height: 154px; }
  .s45 .variety { top: 30px; font-size: 30px; }
  .s45 .quality-band { top: 54px; width: 173px; height: 15px; font-size: 9px; line-height: 15px; }
  .s45 .weight { top: 71px; font-size: 8px; }
  .s45 .brand { top: 113px; }
  .s45 .brand-dot { width: 28px; height: 28px; margin-bottom: 2px; }
  .s45 .brand-name { font-size: 9px; }
  .s45 .web { top: 140px; font-size: 7px; }
  .s45 .contact { left: 12px; top: 97px; font-size: 7.4px; line-height: 9.2px; }
  .s45 .storage { right: 12px; top: 97px; font-size: 7.4px; line-height: 9.2px; }
  .s45 .storage .best-before { margin-top: 6px; font-size: 7px; }
</style>
</head>
<body>
<main class="sheet">

  <p class="size-caption" style="left:172px; top:4px;">ETIKETTEN 100X60 MM</p>

  <section class="label s60 wald" style="left:0; top:40px;">
    <h2 class="variety">WALDHONIG</h2>
    <p class="quality-band">Österreichischer Qualitätshonig</p>
    <p class="weight">150g</p>
    <div class="brand"><span class="brand-dot"></span><span class="brand-name">Lindtal Honig</span></div>
    <p class="web">www.lindtal-honig.at</p>
    <p class="contact">Meisterimkerei Lindtal<br>Birkenweg 12<br>8142 Lindtal<br>Tel: 0664 /31 57 204<br>lindtal-honig@post.at</p>
    <p class="storage">Trocken und vor Wärme<br>geschützt lagern!<span class="best-before">Mindesten haltbar bis:</span></p>
  </section>

  <section class="label s60 bluete" style="left:0; top:262px;">
    <h2 class="variety">BLÜTENHONIG</h2>
    <p class="quality-band">Österreichischer Qualitätshonig</p>
    <p class="weight">150g</p>
    <div class="brand"><span class="brand-dot"></span><span class="brand-name">Lindtal Honig</span></div>
    <p class="web">www.lindtal-honig.at</p>
    <p class="contact">Meisterimkerei Lindtal<br>Birkenweg 12<br>8142 Lindtal<br>Tel: 0664 /31 57 204<br>lindtal-honig@post.at</p>
    <p class="storage">Trocken und vor Wärme<br>geschützt lagern!<span class="best-before">Mindesten haltbar bis:</span></p>
  </section>

  <section class="label s60 creme" style="left:0; top:482px;">
    <h2 class="variety">CREMEHONIG</h2>
    <p class="quality-band">Österreichischer Qualitätshonig</p>
    <p class="weight">150g</p>
    <div class="brand"><span class="brand-dot"></span><span class="brand-name">Lindtal Honig</span></div>
    <p class="web">www.lindtal-honig.at</p>
    <p class="contact">Meisterimkerei Lindtal<br>Birkenweg 12<br>8142 Lindtal<br>Tel: 0664 /31 57 204<br>lindtal-honig@post.at</p>
    <p class="storage">Trocken und vor Wärme<br>geschützt lagern!<span class="best-before">Mindesten haltbar bis:</span></p>
  </section>

  <p class="size-caption" style="left:627px; top:74px;">ETIKETTEN 120X100 MM</p>

  <section class="label s100 wald" style="left:422px; top:111px;">
    <h2 class="variety">WALDHONIG</h2>
    <p class="quality-band">Österreichischer Qualitätshonig</p>
    <p class="weight">150g</p>
    <div class="brand"><span class="brand-dot"></span><span class="brand-name">Lindtal Honig</span></div>
    <p class="web">www.lindtal-honig.at</p>
    <p class="contact">Meisterimkerei Lindtal<br>Birkenweg 12<br>8142 Lindtal<br>Tel: 0664 /31 57 204<br>lindtal-honig@post.at</p>
    <p class="storage">Trocken und vor Wärme<br>geschützt lagern!<span class="best-before">Mindesten haltbar bis:</span></p>
  </section>

  <section class="label s45 wald" style="left:456px; top:491px;">
    <h2 class="variety">WALDHONIG</h2>
    <p class="quality-band">Österreichischer Qualitätshonig</p>
    <p class="weight">150g</p>
    <div class="brand"><span class="brand-dot"></span><span class="brand-name">Lindtal Honig</span></div>
    <p class="web">www.lindtal-honig.at</p>
    <p class="contact">Meisterimkerei Lindtal<br>Birkenweg 12<br>8142 Lindtal<br>Tel: 0664 /31 57 204<br>lindtal-honig@post.at</p>
    <p class="storage">Trocken und vor Wärme<br>geschützt lagern!<span class="best-before">Mindesten haltbar bis:</span></p>
  </section>

  <p class="size-caption" style="left:623px; top:668px;">ETIKETTEN 100X45 MM</p>

</main>
</body>
</html>
```